New Wine Label - Argentinian Malbec 'Brisa Dorada'

I am looking for an exceptional and exciting design for a wine label called 'Brisa Dorada' meaning Golden Breeze or Breeze of Gold. The design must feature the name 'Brisa Dorada', a star logo and the word 'Malbec'. It will also need the words 'Mendoza, Argentina' at the bottom of the label as a prominent piece of information. Please produce the work in size 80mm x 100mm. Feel free to use colour in addition to black/white and ensue that the label is easy to read on a shelf placement.

Target Market(s)

25-50 Year Olds who enjoy great wine that looks and appears interesting and a little different.

Requirements
Must have
• Star Logo
• Word - Malbec
• Words - Mendoza, Argentina
Nice to have
• Background image to label

```html
<!DOCTYPE html>
<html lang="en">
<head>
<meta charset="utf-8">
<title>Brisa Dorada Malbec Label</title>
<link rel="stylesheet" href="https://fonts.googleapis.com/css2?family=Comfortaa:wght@300&display=swap">
<style>
  :root {
    --wine-deep: #1c0909;
    --wine-mid: #300d0c;
    --wine-glow: #43110f;
    --gold: #c9a044;
    --gold-light: #ecd28a;
    --gold-warm: #b8823a;
    --band: #5a3325;
  }
  html, body {
    margin: 0;
    padding: 0;
    width: 960px;
    height: 1200px;
    overflow: hidden;
    background: var(--wine-deep);
  }
  .label {
    position: relative;
    width: 960px;
    height: 1200px;
    overflow: hidden;
    background: radial-gradient(ellipse 75% 55% at 50% 45%, var(--wine-glow) 0%, var(--wine-mid) 50%, var(--wine-deep) 100%);
    font-family: "Comfortaa", sans-serif;
    font-weight: 300;
  }
  .star-field-top {
    position: absolute;
    left: 190px;
    top: 60px;
    width: 540px;
    height: 370px;
    background:
      radial-gradient(circle 95px at 50% 32%, rgba(236,210,138,0.55) 0%, rgba(201,160,68,0.25) 45%, rgba(201,160,68,0) 100%),
      radial-gradient(ellipse 50% 50% at 52% 50%, rgba(201,160,68,0.22) 0%, rgba(184,130,58,0.1) 55%, rgba(184,130,58,0) 100%);
  }
  .brand-mark {
    position: absolute;
    left: 456px;
    top: 150px;
    width: 48px;
    height: 48px;
    border-radius: 50%;
    background: var(--gold);
  }
  .brand-name {
    position: absolute;
    left: 0;
    width: 960px;
    top: 270px;
    margin: 0;
    text-align: center;
    font-size: 48px;
    line-height: 1;
    font-weight: 300;
    color: var(--gold);
  }
  .varietal {
    position: absolute;
    left: 0;
    width: 960px;
    top: 534px;
    margin: 0;
    text-align: center;
    font-size: 100px;
    line-height: 1;
    font-weight: 300;
    letter-spacing: -1px;
    color: var(--gold);
  }
  .star-field-bottom {
    position: absolute;
    left: 0;
    top: 720px;
    width: 960px;
    height: 345px;
    background:
      linear-gradient(to bottom, rgba(201,160,68,0) 0%, rgba(201,160,68,0.1) 45%, rgba(236,210,138,0.32) 100%);
  }
  .origin-band {
    position: absolute;
    left: 0;
    top: 1064px;
    width: 960px;
    height: 66px;
    background: var(--band);
    border-top: 2px solid var(--gold-light);
    border-bottom: 2px solid var(--gold-warm);
    display: flex;
    align-items: center;
    justify-content: center;
  }
  .origin {
    margin: 0;
    font-size: 45px;
    line-height: 1;
    font-weight: 300;
    color: var(--gold);
  }
</style>
</head>
<body>
  <div class="label">
    <div class="star-field-top" role="img" aria-label="Gold shooting star with a trail of scattered small gold stars"></div>
    <div class="brand-mark"></div>
    <h1 class="brand-name">Brisa Dorada</h1>
    <h2 class="varietal">Malbec</h2>
    <div class="star-field-bottom" role="img" aria-label="Field of scattered gold stars rising from the bottom edge"></div>
    <div class="origin-band">
      <p class="origin">Mendoza, Argentina</p>
    </div>
  </div>
</body>
</html>
```